Business Card design for a company called Tully Brook Co

I need a business card design for my oil fired boiler servicing company. I have a logo design already and Im just looking that incorporated into the business card design. card details; Tully Brook Co
Oil Burner Servicing - Mid Ulster Area
Service Engineer - Owen Madler
Mobile 07700914862
email - Tully.Brook.Co@quillpost.net
www.tullybrookco.net
I carry out Servicing, Commissioning, Fault Finding, Warranty Validation
Target Market(s)
home owners with oil fired central heating
Industry/Entity Type
Business
Contact Information for Business Card
Tully Brook Co
Tell. 07700914862
Web: www.tullybrookco.net
email Tully.Brook.Co@Quillpost.Net
Servicing Fault Finding Commissioning Warranty Validation
Look and feel

```html
<!DOCTYPE html>
<html lang="en">
<head>
<meta charset="utf-8">
<title>Tully Brook Co – Business Card</title>
<link href="https://fonts.googleapis.com/css2?family=Arimo:wght@400;700&display=swap" rel="stylesheet">
<style>
  :root {
    --page-bg: #ece9e4;
    --card-bg: #ffffff;
    --brand-green: #56b433;
    --text-green: #5aa932;
    --accent-lime: #a8c43a;
  }
  * { margin: 0; padding: 0; box-sizing: border-box; }
  html, body {
    width: 1200px;
    height: 1000px;
    overflow: hidden;
    background: var(--page-bg);
  }
  .canvas {
    width: 1200px;
    height: 1000px;
    display: flex;
    align-items: center;
    justify-content: center;
  }
  .business-card {
    position: relative;
    width: 900px;
    height: 540px;
    background: var(--card-bg);
    border: 22px solid var(--brand-green);
    box-shadow: 0 6px 24px rgba(0,0,0,0.12);
    font-family: "Arimo", Arial, sans-serif;
    color: var(--text-green);
  }
  .contact-details {
    position: absolute;
    left: 50px;
    top: 40px;
    font-size: 19px;
    font-weight: 700;
    line-height: 1.2;
  }
  .contact-details .line { display: block; }
  .contact-details .group { margin-bottom: 24px; }
  .services {
    position: absolute;
    left: 50px;
    bottom: 40px;
    font-family: "Arimo", Arial, sans-serif;
    font-size: 20px;
    font-weight: 700;
    color: var(--accent-lime);
  }
  .brand-lockup {
    position: absolute;
    right: 60px;
    top: 232px;
    display: flex;
    align-items: center;
    gap: 14px;
  }
  .brand-lockup .brand-dot {
    width: 54px;
    height: 54px;
    border-radius: 50%;
    background: var(--brand-green);
  }
  .brand-lockup .brand-name {
    font-size: 44px;
    font-weight: 700;
    color: var(--brand-green);
  }
</style>
</head>
<body>
<main class="canvas">
  <article class="business-card">
    <div class="contact-details">
      <span class="line group">Tully Brook Co</span>
      <span class="line group">Oil Burner Servicing - Mid Ulster Area</span>
      <span class="line group">Service Engineer - Owen Madler</span>
      <div class="group">
        <span class="line">Tell</span>
        <span class="line">07700914862</span>
      </div>
      <div class="group">
        <span class="line">Web</span>
        <span class="line">www.tullybrookco.net</span>
      </div>
      <div>
        <span class="line">email</span>
        <span class="line">Tully.Brook.Co@Quillpost.Net</span>
      </div>
    </div>
    <p class="services">Servicing, Fault Finding, Commissioning, Warranty Validation</p>
    <div class="brand-lockup">
      <span class="brand-dot"></span>
      <span class="brand-name">Tully Brook Co</span>
    </div>
  </article>
</main>
</body>
</html>
```